Business Card Design using new attached logo

We are a family run Plumbing and Heating firm looking to improve our company image with an improved business card and new logo.We are looking to keep the company colour (Blue) involved in our design

Reason: New logo added which needs to be incorporated on designs

Industry/Entity Type

Business

Contact Information for Business Card

See attachment of all info required.

Requirements
Must have
• We have just picked a new company logo which is attached.
• Could you please provide your business card designs using this logo.
• We are looking for the logo on the back as well as the front with all the info required

```html
<!DOCTYPE html>
<html lang="en">
<head>
<meta charset="utf-8">
<title>Kestrel Heating – Business Cards</title>
<link rel="stylesheet" href="https://fonts.googleapis.com/css2?family=Cinzel:wght@400;600&family=Open+Sans:wght@400;700&display=swap">
<style>
  :root {
    --bg: #e6e6e6;
    --blue-deep: #0a2f9e;
    --blue-mid: #1645c8;
    --blue-bright: #2356e0;
    --blue-line: #7fa2f0;
    --white: #ffffff;
    --ink-light: #e9eefc;
  }
  * { margin: 0; padding: 0; box-sizing: border-box; }
  html, body { width: 1200px; height: 871px; overflow: hidden; background: var(--bg); }
  .canvas { position: relative; width: 1200px; height: 871px; }

  .card {
    position: absolute;
    width: 540px;
    height: 318px;
    border-radius: 4px;
    overflow: hidden;
    box-shadow: 0 6px 18px rgba(0,0,0,0.18);
  }

  .brand-name {
    font-family: "Open Sans", sans-serif;
    font-weight: 400;
    font-size: 26px;
    letter-spacing: 0.5px;
    white-space: nowrap;
  }

  /* Back of card */
  .card-back {
    left: 70px; top: 110px;
    background: linear-gradient(160deg, var(--blue-bright) 0%, var(--blue-mid) 50%, var(--blue-deep) 100%);
    display: flex; align-items: center; justify-content: center;
  }
  .card-back .brand-name { color: var(--ink-light); }

  /* Front of card */
  .card-front {
    left: 590px; top: 440px;
    background: var(--white);
  }
  .front-header {
    position: absolute; left: 0; top: 0; width: 100%; height: 110px;
    display: flex; align-items: center; justify-content: center;
    background: linear-gradient(180deg, #ffffff 0%, #f1f3f8 100%);
  }
  .card-front .brand-name { color: var(--blue-mid); font-size: 24px; }
  .front-rule {
    position: absolute; left: 0; top: 110px; width: 100%; height: 5px;
    background: var(--blue-line);
  }
  .front-body {
    position: absolute; left: 0; top: 115px; width: 100%; height: 203px;
    background: linear-gradient(170deg, var(--blue-bright) 0%, var(--blue-mid) 45%, var(--blue-deep) 100%);
    color: var(--white);
  }
  .person { position: absolute; left: 30px; top: 22px; }
  .person-name {
    font-family: "Cinzel", serif; font-weight: 600; font-size: 17px; letter-spacing: 1px;
  }
  .person-role {
    font-family: "Cinzel", serif; font-weight: 400; font-size: 12px; letter-spacing: 1px; margin-top: 2px;
  }
  .contact {
    position: absolute; left: 270px; top: 22px;
    font-family: "Open Sans", sans-serif; font-size: 11px; line-height: 17px;
  }
  .contact-company { font-weight: 700; }
  .contact-list { list-style: none; margin-top: 8px; }
  .contact-list li { display: flex; align-items: center; gap: 10px; }
  .contact-list svg { width: 12px; height: 12px; fill: none; stroke: var(--white); stroke-width: 1.4; flex-shrink: 0; }
</style>
</head>
<body>
<main class="canvas">

  <section class="card card-back" aria-label="Card back">
    <span class="brand-name">Kestrel Heating</span>
  </section>

  <section class="card card-front" aria-label="Card front">
    <header class="front-header">
      <span class="brand-name">Kestrel Heating</span>
    </header>
    <div class="front-rule"></div>
    <div class="front-body">
      <div class="person">
        <p class="person-name">DANIEL HART</p>
        <p class="person-role">DIRECTOR</p>
      </div>
      <div class="contact">
        <p class="contact-company">KESTREL HEATING</p>
        <p>14 Mill Parade</p>
        <p>elm road, fenwick, surrey</p>
        <ul class="contact-list">
          <li>
            <svg viewBox="0 0 12 12" aria-hidden="true"><path d="M1 4 Q6 0 11 4 L9 5 L8 3.5 Q6 3 4 3.5 L3 5 Z"/><rect x="3" y="6" width="6" height="5"/></svg>
            <span>020 7946 0123</span>
          </li>
          <li>
            <svg viewBox="0 0 12 12" aria-hidden="true"><rect x="3" y="1" width="6" height="4"/><rect x="1" y="5" width="10" height="4"/><rect x="3" y="8" width="6" height="3"/></svg>
            <span>020 7946 0456</span>
          </li>
          <li>
            <svg viewBox="0 0 12 12" aria-hidden="true"><rect x="3" y="1" width="6" height="10" rx="1"/><line x1="5" y1="9.2" x2="7" y2="9.2"/></svg>
            <span>07700 900712</span>
          </li>
          <li>
            <svg viewBox="0 0 12 12" aria-hidden="true"><rect x="1" y="2.5" width="10" height="7"/><path d="M1 2.5 L6 7 L11 2.5"/></svg>
            <span>danielhart@kestrelheating.co.uk</span>
          </li>
        </ul>
      </div>
    </div>
  </section>

</main>
</body>
</html>
```